Interior Decorating business - Logo & Stationery

"Velvet Lantern" is a newly established interior decorating company, based in Sydney, providing interior decorating, colour consulting and property styling services to residential and commercial clients.

We require a logo and stationery design (double-sided business card, A4 letterhead and with compliments slip (210mm X 95mm))

Letterhead information and with compliments slip:
Address - 22/31-33 Thornbury Rd, Kelvin Grove NSW 2098
Phone - (02)9617 4280
Mobile - 0427 386 509
Email - maeve@velvetlantern.com.au
Web - www.velvetlantern.com.au
ABN - 47392815064

Business Cards should be double sided and are to include;
Maeve Hollis
Director

with email address, mobile number, website as listed above

They also need to include services offered i.e. Interior Decorating, Colour Consulting, Property Styling

Please note that the current content on the website will be updated, so disregard logo and content currently on the website.

Target Market(s)

Target market is two-fold - residential clients (primarily homeowners with pride in their homes) and commerical clients (specifically business owners of retail shops and cafes and property developers)

Industry/Entity Type

Residential

```html
<!DOCTYPE html>
<html lang="en">
<head>
<meta charset="utf-8">
<title>Velvet Lantern — Letterhead</title>
<link rel="stylesheet" href="https://fonts.googleapis.com/css2?family=Arimo:wght@400&display=swap">
<style>
  :root {
    --paper: #ffffff;
    --ink-blue: #1b5fae;
    --brand-blue: #1e8ad6;
    --wave-deep: #1466c2;
    --wave-mid: #3fa3e3;
    --wave-light: #a9dcf5;
    --wave-pale: #e3f4fc;
  }
  html, body {
    margin: 0;
    padding: 0;
    overflow: hidden;
    background: var(--paper);
  }
  .letterhead {
    position: relative;
    width: 847px;
    height: 1200px;
    background: var(--paper);
    overflow: hidden;
    font-family: "Arimo", Arial, sans-serif;
  }
  .header-artwork {
    position: absolute;
    top: 0;
    left: 0;
    width: 847px;
    height: 360px;
  }
  .footer-artwork {
    position: absolute;
    left: 0;
    bottom: 0;
    width: 847px;
    height: 180px;
  }
  .brand-name {
    position: absolute;
    top: 28px;
    right: 48px;
    margin: 0;
    font-size: 74px;
    font-weight: 400;
    line-height: 1;
    color: var(--brand-blue);
    letter-spacing: 1px;
  }
  .contact-details {
    position: absolute;
    top: 168px;
    left: 14px;
    margin: 0;
    font-style: normal;
    font-size: 17px;
    line-height: 20.5px;
    color: var(--ink-blue);
  }
  .contact-details span {
    display: block;
  }
</style>
</head>
<body>
  <main class="letterhead">
    <svg class="header-artwork" viewBox="0 0 847 360" role="img" aria-label="Flowing blue wave band with overlapping swirl circles across the top of the page">
      <defs>
        <linearGradient id="headerWave" x1="0" y1="0" x2="1" y2="0">
          <stop offset="0" stop-color="#bfe6f8"/>
          <stop offset="0.5" stop-color="#5fb6ea"/>
          <stop offset="1" stop-color="#2a86d4"/>
        </linearGradient>
        <linearGradient id="headerMist" x1="0" y1="0" x2="1" y2="1">
          <stop offset="0" stop-color="#e3f4fc"/>
          <stop offset="1" stop-color="#9fd6f3"/>
        </linearGradient>
      </defs>
      <path d="M0 0 H847 V250 C760 300 650 250 560 210 C470 170 380 150 250 150 C150 150 60 140 0 120 Z" fill="url(#headerMist)"/>
      <path d="M0 135 C120 160 260 160 380 170 C520 182 620 250 700 300 C760 335 815 335 847 320 V285 C800 300 750 290 690 255 C600 205 500 155 380 150 C250 145 110 140 0 110 Z" fill="url(#headerWave)"/>
    </svg>

    <h1 class="brand-name">Velvet Lantern</h1>

    <address class="contact-details">
      <span>22/31-33 Thornbury Rd,</span>
      <span>Kelvin Grove NSW 2098</span>
      <span>(02)9617 4280</span>
      <span>0427 386 509</span>
      <span>maeve@velvetlantern.com.au</span>
      <span>www.velvetlantern.com.au</span>
      <span>ABN - 47392815064</span>
    </address>

    <svg class="footer-artwork" viewBox="0 0 847 180" role="img" aria-label="Blue swirl circles and sweeping wave lines along the bottom edge">
      <defs>
        <linearGradient id="footerWave" x1="0" y1="0" x2="1" y2="0">
          <stop offset="0" stop-color="#2a7fd0"/>
          <stop offset="0.55" stop-color="#6cc0ec"/>
          <stop offset="1" stop-color="#d6effb"/>
        </linearGradient>
      </defs>
      <path d="M0 60 C150 30 300 20 450 60 C600 100 720 130 847 120 V180 H0 Z" fill="url(#footerWave)"/>
    </svg>
  </main>
</body>
</html>
```